Design images for a digital product for ecommerce

We sell travel eSIMs on our website, Korvanta and Tradlio and need product images. Currently our images are mostly flags and maps of the country sims we are selling. This however doesn't look good on Tradlio or Korvanta listings. It needs to look more like a product.
An idea I have would be perhaps to make it look like a passport that has the eSIM name at the front (just like the country name on our passport). But we still need to bring in the element of eSIM product.
This is just a suggestion and I am opened to any ideas to enhance the product listings.
As we have several products, ideally we would receive a variation of colours and styles we can then edit ourselves to suit each product.
It will need to match a little bit the branding guidelines of our website.
https://veltrinemobile.com.au/product-category/travel-esim/

```html
<!DOCTYPE html>
<html lang="en">
<head>
<meta charset="UTF-8">
<title>Veltrine Mobile Travel eSIM Range</title>
<link rel="stylesheet" href="https://fonts.googleapis.com/css2?family=Arimo:wght@400;700&display=swap">
<style>
  :root {
    --canvas: #ffffff;
    --card-red: #f3242b;
    --card-red-light: #ff6161;
    --card-red-deep: #e51a22;
    --ink: #1b1b1b;
    --white: #ffffff;
    --accent-yellow: #ffe31a;
  }
  * { margin: 0; padding: 0; box-sizing: border-box; }
  html, body { width: 675px; height: 1200px; overflow: hidden; background: var(--canvas); }
  body { font-family: "Arimo", Arial, sans-serif; position: relative; }

  .product-grid { position: absolute; left: 70px; top: 2px; display: grid;
    grid-template-columns: 245px 245px; column-gap: 24px; row-gap: 19px; }

  .esim-card { position: relative; width: 245px; height: 266px; border-radius: 20px; overflow: hidden;
    background:
      linear-gradient(200deg, var(--card-red-light) 0%, rgba(255,97,97,0) 38%),
      linear-gradient(160deg, var(--card-red) 0%, var(--card-red-deep) 100%); }
  .esim-card::after { content: ""; position: absolute; right: -60px; top: 40px; width: 240px; height: 120px;
    background: rgba(255,255,255,0.10); transform: rotate(-28deg); border-radius: 50%; }

  .hang-hole { position: absolute; left: 97px; top: 10px; width: 69px; height: 14px; border-radius: 7px; background: var(--white); z-index: 2; }

  .brand { position: absolute; left: 16px; top: 14px; display: flex; align-items: center; gap: 4px;
    color: var(--white); font-weight: 700; font-size: 13px; z-index: 2; }
  .brand-dot { width: 8px; height: 8px; border-radius: 50%; background: var(--white); }

  .esim-badge { position: absolute; left: 178px; top: 37px; width: 55px; height: 19px; border: 1.5px dashed var(--accent-yellow);
    color: var(--accent-yellow); font-weight: 700; font-size: 13px; line-height: 16px; text-align: center; z-index: 2; }

  .destination-art { position: absolute; left: 0; top: 0; width: 245px; height: 266px; z-index: 1; }

  .region-name { position: absolute; left: 22px; top: 118px; width: 130px; text-align: center; color: var(--white);
    font-weight: 700; font-size: 26px; line-height: 26px; text-shadow: 0 1px 3px rgba(0,0,0,0.45); z-index: 3; }
  .region-name small { display: block; font-size: 19px; line-height: 22px; }
  .region-name--dark { color: var(--ink); text-shadow: -1px -1px 0 #fff, 1px -1px 0 #fff, -1px 1px 0 #fff, 1px 1px 0 #fff; }

  .product-copy { position: absolute; left: 143px; top: 76px; color: var(--ink); font-size: 14px; line-height: 17px; z-index: 3; }
  .product-copy strong { display: block; font-weight: 700; }
  .product-copy .areas { display: block; color: var(--white); font-size: 16px; line-height: 20px; font-weight: 700; }

  .tagline { position: absolute; left: 150px; top: 216px; color: var(--accent-yellow); font-weight: 700; font-size: 9.5px; z-index: 3; }

  .feature-strip { position: absolute; left: 72px; top: 236px; width: 165px; height: 21px; border: 1px dashed var(--white);
    border-radius: 11px; display: flex; align-items: center; justify-content: space-around; padding: 0 4px; z-index: 3; }
  .feature { display: flex; align-items: center; gap: 2px; color: var(--white); font-size: 4.6px; font-weight: 700; white-space: nowrap; }
  .feature-icon { width: 11px; height: 11px; }
</style>
</head>
<body>
<main class="product-grid">

  <!-- South East Asia -->
  <article class="esim-card">
    <span class="hang-hole"></span>
    <div class="brand"><span class="brand-dot"></span>Veltrine</div>
    <div class="esim-badge">eSIM</div>
    <svg class="destination-art" viewBox="0 0 245 266" role="img" aria-label="Photo of a golden pagoda under a blue sky">
      <defs><linearGradient id="art-sea" x1="0" y1="0" x2="0" y2="1"><stop offset="0" stop-color="#9fb9d6"/><stop offset="0.55" stop-color="#d6a43a"/><stop offset="1" stop-color="#4a5a34"/></linearGradient></defs>
      <path d="M18 62 C6 62 2 70 2 84 L2 226 C2 242 12 250 26 243 L138 172 C151 164 151 148 138 140 L30 66 C26 63 22 62 18 62 Z" fill="url(#art-sea)" stroke="#d8a63e" stroke-width="5"/>
    </svg>
    <div class="region-name">South<small>East Asia</small></div>
    <div class="product-copy">Roaming Data<strong>ESIM</strong><span class="areas">(7 Areas)</span></div>
    <div class="tagline">Connect any Time</div>
    <div class="feature-strip">
      <span class="feature"><svg class="feature-icon" viewBox="0 0 12 12"><circle cx="6" cy="6" r="6" fill="#fff"/><circle cx="6" cy="6" r="3" fill="none" stroke="#e51a22" stroke-width="1"/></svg>Global Coverage</span>
      <span class="feature"><svg class="feature-icon" viewBox="0 0 12 12"><circle cx="6" cy="6" r="6" fill="#fff"/><path d="M4 3v6M4 6h4" stroke="#e51a22" stroke-width="1.2"/></svg>Easy Activation</span>
      <span class="feature"><svg class="feature-icon" viewBox="0 0 12 12"><circle cx="6" cy="6" r="6" fill="#fff"/><path d="M6 3v6M4.5 4.5h3M4.5 7.5h3" stroke="#e51a22" stroke-width="1"/></svg>Cost Effective</span>
    </div>
  </article>

  <!-- China -->
  <article class="esim-card">
    <span class="hang-hole"></span>
    <div class="brand"><span class="brand-dot"></span>Veltrine</div>
    <div class="esim-badge">eSIM</div>
    <svg class="destination-art" viewBox="0 0 245 266" role="img" aria-label="Photo of a red Chinese pavilion among green trees">
      <defs><linearGradient id="art-china" x1="0" y1="0" x2="0" y2="1"><stop offset="0" stop-color="#e8ecef"/><stop offset="0.45" stop-color="#b23a2e"/><stop offset="1" stop-color="#3f6b2e"/></linearGradient></defs>
      <path d="M18 62 C6 62 2 70 2 84 L2 226 C2 242 12 250 26 243 L138 172 C151 164 151 148 138 140 L30 66 C26 63 22 62 18 62 Z" fill="url(#art-china)" stroke="#b8342f" stroke-width="5"/>
    </svg>
    <div class="region-name region-name--dark" style="left:50px;top:130px;">china</div>
    <div class="product-copy" style="top:78px;left:130px;font-size:15px;">Roaming Data<strong>ESIM</strong></div>
    <div class="tagline">Connect any Time</div>
    <div class="feature-strip">
      <span class="feature"><svg class="feature-icon" viewBox="0 0 12 12"><circle cx="6" cy="6" r="6" fill="#fff"/><circle cx="6" cy="6" r="3" fill="none" stroke="#e51a22" stroke-width="1"/></svg>Global Coverage</span>
      <span class="feature"><svg class="feature-icon" viewBox="0 0 12 12"><circle cx="6" cy="6" r="6" fill="#fff"/><path d="M4 3v6M4 6h4" stroke="#e51a22" stroke-width="1.2"/></svg>Easy Activation</span>
      <span class="feature"><svg class="feature-icon" viewBox="0 0 12 12"><circle cx="6" cy="6" r="6" fill="#fff"/><path d="M6 3v6M4.5 4.5h3M4.5 7.5h3" stroke="#e51a22" stroke-width="1"/></svg>Cost Effective</span>
    </div>
  </article>

  <!-- Global -->
  <article class="esim-card">
    <span class="hang-hole"></span>
    <div class="brand"><span class="brand-dot"></span>Veltrine</div>
    <div class="esim-badge">eSIM</div>
    <svg class="destination-art" viewBox="0 0 245 266" role="img" aria-label="Photo of many national flags hanging in rows">
      <defs><linearGradient id="art-global" x1="0" y1="0" x2="1" y2="1"><stop offset="0" stop-color="#c94a3a"/><stop offset="0.4" stop-color="#e9e4da"/><stop offset="0.7" stop-color="#3c6aa8"/><stop offset="1" stop-color="#2f7a4a"/></linearGradient></defs>
      <path d="M18 62 C6 62 2 70 2 84 L2 226 C2 242 12 250 26 243 L138 172 C151 164 151 148 138 140 L30 66 C26 63 22 62 18 62 Z" fill="url(#art-global)" stroke="#d4a03a" stroke-width="5"/>
    </svg>
    <div class="region-name" style="top:140px;">Global</div>
    <div class="product-copy" style="left:138px;top:74px;">Roaming <b>ESIM</b><span class="areas" style="margin-top:6px;">(130+ Areas)</span></div>
    <div class="tagline">Connect any Time</div>
    <div class="feature-strip">
      <span class="feature"><svg class="feature-icon" viewBox="0 0 12 12"><circle cx="6" cy="6" r="6" fill="#fff"/><circle cx="6" cy="6" r="3" fill="none" stroke="#e51a22" stroke-width="1"/></svg>Global Coverage</span>
      <span class="feature"><svg class="feature-icon" viewBox="0 0 12 12"><circle cx="6" cy="6" r="6" fill="#fff"/><path d="M4 3v6M4 6h4" stroke="#e51a22" stroke-width="1.2"/></svg>Easy Activation</span>
      <span class="feature"><svg class="feature-icon" viewBox="0 0 12 12"><circle cx="6" cy="6" r="6" fill="#fff"/><path d="M6 3v6M4.5 4.5h3M4.5 7.5h3" stroke="#e51a22" stroke-width="1"/></svg>Cost Effective</span>
    </div>
  </article>

  <!-- Middle East -->
  <article class="esim-card">
    <span class="hang-hole"></span>
    <div class="brand"><span class="brand-dot"></span>Veltrine</div>
    <div class="esim-badge">eSIM</div>
    <svg class="destination-art" viewBox="0 0 245 266" role="img" aria-label="Photo of a coastal city skyline by the sea">
      <defs><linearGradient id="art-mideast" x1="0" y1="0" x2="0" y2="1"><stop offset="0" stop-color="#c9d3da"/><stop offset="0.5" stop-color="#5f8ea3"/><stop offset="1" stop-color="#3e4c55"/></linearGradient></defs>
      <path d="M18 62 C6 62 2 70 2 84 L2 226 C2 242 12 250 26 243 L138 172 C151 164 151 148 138 140 L30 66 C26 63 22 62 18 62 Z" fill="url(#art-mideast)" stroke="#1c6b72" stroke-width="5"/>
    </svg>
    <div class="region-name" style="left:30px;top:124px;">Middle<br>East</div>
    <div class="product-copy" style="left:143px;top:74px;">Roaming Data<strong>ESIM</strong><span class="areas">(13 Areas)</span></div>
    <div class="tagline">Connect any Time</div>
    <div class="feature-strip">
      <span class="feature"><svg class="feature-icon" viewBox="0 0 12 12"><circle cx="6" cy="6" r="6" fill="#fff"/><circle cx="6" cy="6" r="3" fill="none" stroke="#e51a22" stroke-width="1"/></svg>Global Coverage</span>
      <span class="feature"><svg class="feature-icon" viewBox="0 0 12 12"><circle cx="6" cy="6" r="6" fill="#fff"/><path d="M4 3v6M4 6h4" stroke="#e51a22" stroke-width="1.2"/></svg>Easy Activation</span>
      <span class="feature"><svg class="feature-icon" viewBox="0 0 12 12"><circle cx="6" cy="6" r="6" fill="#fff"/><path d="M6 3v6M4.5 4.5h3M4.5 7.5h3" stroke="#e51a22" stroke-width="1"/></svg>Cost Effective</span>
    </div>
  </article>

  <!-- North America -->
  <article class="esim-card">
    <span class="hang-hole"></span>
    <div class="brand"><span class="brand-dot"></span>Veltrine</div>
    <div class="esim-badge">eSIM</div>
    <svg class="destination-art" viewBox="0 0 245 266" role="img" aria-label="Photo of a harbour statue with a city skyline behind">
      <defs><linearGradient id="art-namerica" x1="0" y1="0" x2="0" y2="1"><stop offset="0" stop-color="#d9e2ea"/><stop offset="0.5" stop-color="#8aa3b8"/><stop offset="1" stop-color="#5b6e55"/></linearGradient></defs>
      <path d="M18 62 C6 62 2 70 2 84 L2 226 C2 242 12 250 26 243 L138 172 C151 164 151 148 138 140 L30 66 C26 63 22 62 18 62 Z" fill="url(#art-namerica)" stroke="#9fb3c8" stroke-width="5"/>
    </svg>
    <div class="region-name" style="left:24px;top:124px;">North<small>America</small></div>
    <div class="product-copy" style="left:145px;top:78px;">Roaming Data<strong>ESIM</strong><span class="areas">(3 Areas)</span></div>
    <div class="tagline">Connect any Time</div>
    <div class="feature-strip">
      <span class="feature"><svg class="feature-icon" viewBox="0 0 12 12"><circle cx="6" cy="6" r="6" fill="#fff"/><circle cx="6" cy="6" r="3" fill="none" stroke="#e51a22" stroke-width="1"/></svg>Global Coverage</span>
      <span class="feature"><svg class="feature-icon" viewBox="0 0 12 12"><circle cx="6" cy="6" r="6" fill="#fff"/><path d="M4 3v6M4 6h4" stroke="#e51a22" stroke-width="1.2"/></svg>Easy Activation</span>
      <span class="feature"><svg class="feature-icon" viewBox="0 0 12 12"><circle cx="6" cy="6" r="6" fill="#fff"/><path d="M6 3v6M4.5 4.5h3M4.5 7.5h3" stroke="#e51a22" stroke-width="1"/></svg>Cost Effective</span>
    </div>
  </article>

  <!-- South America -->
  <article class="esim-card">
    <span class="hang-hole"></span>
    <div class="brand"><span class="brand-dot"></span>Veltrine</div>
    <div class="esim-badge">eSIM</div>
    <svg class="destination-art" viewBox="0 0 245 266" role="img" aria-label="Photo of a green mountain above a bay">
      <defs><linearGradient id="art-samerica" x1="0" y1="0" x2="0" y2="1"><stop offset="0" stop-color="#cfd9d4"/><stop offset="0.45" stop-color="#6f9b8a"/><stop offset="1" stop-color="#3f6a2a"/></linearGradient></defs>
      <path d="M18 62 C6 62 2 70 2 84 L2 226 C2 242 12 250 26 243 L138 172 C151 164 151 148 138 140 L30 66 C26 63 22 62 18 62 Z" fill="url(#art-samerica)" stroke="#7cc4b8" stroke-width="5"/>
    </svg>
    <div class="region-name" style="left:28px;top:127px;">South<small>America</small></div>
    <div class="product-copy" style="left:140px;top:78px;">Roaming Data<strong>ESIM</strong><span class="areas">(15+ Areas)</span></div>
    <div class="tagline">Connect any Time</div>
    <div class="feature-strip">
      <span class="feature"><svg class="feature-icon" viewBox="0 0 12 12"><circle cx="6" cy="6" r="6" fill="#fff"/><circle cx="6" cy="6" r="3" fill="none" stroke="#e51a22" stroke-width="1"/></svg>Global Coverage</span>
      <span class="feature"><svg class="feature-icon" viewBox="0 0 12 12"><circle cx="6" cy="6" r="6" fill="#fff"/><path d="M4 3v6M4 6h4" stroke="#e51a22" stroke-width="1.2"/></svg>Easy Activation</span>
      <span class="feature"><svg class="feature-icon" viewBox="0 0 12 12"><circle cx="6" cy="6" r="6" fill="#fff"/><path d="M6 3v6M4.5 4.5h3M4.5 7.5h3" stroke="#e51a22" stroke-width="1"/></svg>Cost Effective</span>
    </div>
  </article>

  <!-- Asia -->
  <article class="esim-card">
    <span class="hang-hole"></span>
    <div class="brand"><span class="brand-dot"></span>Veltrine</div>
    <div class="esim-badge">eSIM</div>
    <svg class="destination-art" viewBox="0 0 245 266" role="img" aria-label="Photo of a river boat with a city skyline and a lantern">
      <defs><linearGradient id="art-asia" x1="0" y1="0" x2="0" y2="1"><stop offset="0" stop-color="#a7bfd8"/><stop offset="0.55" stop-color="#7a5a3a"/><stop offset="1" stop-color="#3f5a3a"/></linearGradient></defs>
      <path d="M18 62 C6 62 2 70 2 84 L2 226 C2 242 12 250 26 243 L138 172 C151 164 151 148 138 140 L30 66 C26 63 22 62 18 62 Z" fill="url(#art-asia)" stroke="#3f4c6b" stroke-width="5"/>
    </svg>
    <div class="region-name" style="left:48px;top:143px;">Asia</div>
    <div class="product-copy" style="left:145px;top:76px;">Roaming Data<strong>ESIM</strong><span class="areas">(20+ Areas)</span></div>
    <div class="tagline">Connect any Time</div>
    <div class="feature-strip">
      <span class="feature"><svg class="feature-icon" viewBox="0 0 12 12"><circle cx="6" cy="6" r="6" fill="#fff"/><circle cx="6" cy="6" r="3" fill="none" stroke="#e51a22" stroke-width="1"/></svg>Global Coverage</span>
      <span class="feature"><svg class="feature-icon" viewBox="0 0 12 12"><circle cx="6" cy="6" r="6" fill="#fff"/><path d="M4 3v6M4 6h4" stroke="#e51a22" stroke-width="1.2"/></svg>Easy Activation</span>
      <span class="feature"><svg class="feature-icon" viewBox="0 0 12 12"><circle cx="6" cy="6" r="6" fill="#fff"/><path d="M6 3v6M4.5 4.5h3M4.5 7.5h3" stroke="#e51a22" stroke-width="1"/></svg>Cost Effective</span>
    </div>
  </article>

  <!-- Europe -->
  <article class="esim-card">
    <span class="hang-hole"></span>
    <div class="brand"><span class="brand-dot"></span>Veltrine</div>
    <div class="esim-badge">eSIM</div>
    <svg class="destination-art" viewBox="0 0 245 266" role="img" aria-label="Photo of an iron lattice tower under a blue sky">
      <defs><linearGradient id="art-europe" x1="0" y1="0" x2="0" y2="1"><stop offset="0" stop-color="#4f86c8"/><stop offset="0.55" stop-color="#a9c4e2"/><stop offset="1" stop-color="#4f7a3a"/></linearGradient></defs>
      <path d="M18 62 C6 62 2 70 2 84 L2 226 C2 242 12 250 26 243 L138 172 C151 164 151 148 138 140 L30 66 C26 63 22 62 18 62 Z" fill="url(#art-europe)" stroke="#e8a92a" stroke-width="5"/>
    </svg>
    <div class="region-name" style="left:30px;top:140px;">Europe</div>
    <div class="product-copy" style="left:143px;top:76px;">Data Roaming<strong>ESIM</strong><span class="areas">(40+ Areas)</span></div>
    <div class="tagline">Connect any Time</div>
    <div class="feature-strip">
      <span class="feature"><svg class="feature-icon" viewBox="0 0 12 12"><circle cx="6" cy="6" r="6" fill="#fff"/><circle cx="6" cy="6" r="3" fill="none" stroke="#e51a22" stroke-width="1"/></svg>Global Coverage</span>
      <span class="feature"><svg class="feature-icon" viewBox="0 0 12 12"><circle cx="6" cy="6" r="6" fill="#fff"/><path d="M4 3v6M4 6h4" stroke="#e51a22" stroke-width="1.2"/></svg>Easy Activation</span>
      <span class="feature"><svg class="feature-icon" viewBox="0 0 12 12"><circle cx="6" cy="6" r="6" fill="#fff"/><path d="M6 3v6M4.5 4.5h3M4.5 7.5h3" stroke="#e51a22" stroke-width="1"/></svg>Cost Effective</span>
    </div>
  </article>

</main>
</body>
</html>
```